redesign my website coralhopvoyages.net and make it user friendly

I already have a website, coralhopvoyages.net, and want a redesign in WordPress with Elementor Pro, using the same text/content. The goal is to improve:

Design quality (colors, fonts, spacing, visual flow)
User experience (easy navigation, clear offers)
Conversion readiness (calls-to-action, trust signals, booking flow)
Technical side (SEO basics, fast speed, full mobile responsiveness)

The site should look modern, clean, fun, engaging, interactive and optimized for speed and usability.

I would like the 11 page to be consolidate dto 6 as follows: Home (main landing, highlights)

Sailboat Trips (all packages, itineraries, pricing)
Boats (fleet details, features, photos)
How It Works (booking process, FAQs, travel info, what to expect)
Blog
Contact Us (form, WhatsApp, phone, etc.)

Target Market(s)

sailboat trip customers for San Blas Islands in Panama

Industry/Entity Type

Travel, Boat Tour Agency

Coding

Coded - Design and coding required

Number of Pages Required

3 page

Font styles to use
Sans Serif
Other font styles liked:
• Oswalg and sans serif

Colors
0054AA
0677BA
7BADD7
CADEEF
E8F1F8
0094D4
00A9DD
6FCCEA
C7EBF8
E9F6FB
FFC000
F8CF3A
FAE287
FDF2CF
FEFAEE
F0912C
F2A743
F7CA91
FBE8D2
FDF5EE

Requirements
Must have
• Home (main landing, highlights) Sailboat Trips (all packages, itineraries, pricing) Boats (fleet details, features, photos) How It Works (booking process, FAQs, travel info, what to expect) Blog (updates, travel tips, inspiration) Contact Us (form, WhatsApp, phone, etc.)
Nice to have
• I want it to look professionla and be very user friendy to entice people to contact me to book boat trips
Should not have
• a store

```html
<!DOCTYPE html>
<html lang="en">
<head>
<meta charset="utf-8">
<title>Coral Hop Voyages — Panama Sailing Charters</title>
<link href="https://fonts.googleapis.com/css2?family=DM+Serif+Text&family=Poppins:wght@400;500;600;700&family=Allura&display=swap" rel="stylesheet">
<style>
:root{
  --navy:#141b3a;
  --navy-deep:#0f1530;
  --ink:#1b1f2e;
  --text:#555b6b;
  --muted:#8a90a0;
  --blue:#2f5bd6;
  --brand-blue:#0054AA;
  --sky:#0094D4;
  --pale:#f3f5fa;
  --line:#e3e6ee;
  --yellow:#FFC000;
  --orange:#F0912C;
  --red:#e8473a;
  --white:#ffffff;
}
*{box-sizing:border-box;margin:0;padding:0}
html,body{width:1200px;height:4402px;overflow:hidden}
body{font-family:"Poppins",sans-serif;color:var(--text);background:var(--white);position:relative}
.abs{position:absolute}
section,header,footer,nav{position:relative;display:block;width:1200px}
.serif{font-family:"DM Serif Text",serif;color:var(--ink);font-weight:400}
.script{font-family:"Allura",cursive;color:var(--blue)}
.photo{position:absolute;display:block}

/* top bar */
.topbar{height:29px;background:var(--navy-deep);color:#cfd3e0;font-size:8px}
.topbar .ask{left:38px;top:9px}
.topbar .ask b{color:var(--yellow);font-weight:500}
.topbar .tag{left:0;right:0;top:9px;text-align:center;color:var(--yellow)}
.topbar .social{right:90px;top:9px;display:flex;gap:9px}
.topbar .social i{width:10px;height:10px;border-radius:50%;background:#cfd3e0;display:block}
.topbar .lang{right:38px;top:9px}

/* nav */
.nav{height:65px;background:var(--white)}
.logo{left:52px;top:19px;display:flex;align-items:center;gap:10px}
.logo .mark{width:26px;height:26px;border-radius:50%;background:var(--sky)}
.logo .name{font-size:19px;font-weight:600;color:var(--ink)}
.menu{right:200px;top:26px;display:flex;gap:26px;font-size:10.5px;font-weight:500;color:var(--ink)}
.cta-nav{left:1032px;top:18px;width:128px;height:32px;background:var(--yellow);color:var(--ink);font-size:9px;font-weight:600;display:flex;align-items:center;justify-content:center}

/* hero */
.hero{height:431px;overflow:hidden}
.hero .bg{inset:0;background:radial-gradient(ellipse at 30% 30%,#3b6f8a 0%,#1d4460 35%,#0f2a42 70%,#0b1e33 100%)}
.hero .script{left:0;right:0;top:130px;text-align:center;color:var(--white);font-size:28px}
.hero h1{position:absolute;left:0;right:0;top:160px;text-align:center;color:var(--white);font-size:49px}
.search{left:250px;top:284px;width:699px;height:57px;background:var(--white);display:flex}
.search .field{flex:0 0 191px;display:flex;align-items:center;gap:12px;padding-left:14px;border-right:1px solid var(--line)}
.search .field:nth-child(3){flex-basis:144px;border:0}
.search .ic{width:12px;height:12px;border:1.5px solid var(--muted);border-radius:2px}
.search .lbl{font-size:10px;font-weight:600;color:var(--ink)}
.search .val{font-size:9px;color:var(--muted)}
.search .go{flex:1;background:var(--blue);color:var(--white);font-size:10px;font-weight:500;display:flex;align-items:center;justify-content:center;gap:6px}

/* about */
.about{height:625px}
.about .txt{left:667px;top:70px;width:285px}
.about .script{font-size:26px}
.about h2{font-size:28px;line-height:34px;margin-top:2px}
.about p{font-size:8.6px;line-height:14px;margin-top:14px}
.btn-blue{display:inline-flex;align-items:center;justify-content:center;width:105px;height:34px;background:var(--blue);color:var(--white);font-size:9.5px;font-weight:600;margin-top:22px}

/* section heading */
.sec-head{text-align:center}
.sec-head .script{font-size:26px;display:block}
.sec-head h2{font-size:28px;margin-top:-2px}

/* services */
.services-head{height:98px;padding-top:12px}
.services{height:483px;background:var(--pale)}
.svc{top:37px;width:265px;height:414px;background:var(--white);text-align:center}
.svc .pic{height:265px;position:relative}
.svc h3{font-size:20px;line-height:24px;margin-top:20px;padding:0 30px}
.svc p{font-size:8.5px;line-height:15px;color:var(--ink);padding:0 16px;margin-top:6px}

/* catamarans */
.fleet{height:1152px}
.fleet .sec-head{padding-top:44px}
.cat{top:144px;width:265px;height:357px;border:1px solid var(--line);background:var(--white)}
.cat .pic{position:relative;height:207px}
.cat .badge{position:absolute;left:20px;top:20px;background:var(--red);color:var(--white);font-size:7.5px;padding:2px 6px}
.cat .heart{position:absolute;right:18px;top:16px;width:14px;height:14px}
.cat .added{position:absolute;right:14px;top:18px;color:var(--white);font-size:9.5px;text-align:right;line-height:13px}
.cat .stats{position:absolute;left:16px;right:14px;bottom:16px;display:flex;justify-content:space-between;color:var(--white);font-size:9px}
.cat h3{font-family:"Poppins",sans-serif;font-size:16px;font-weight:500;color:var(--ink);margin:18px 0 0 20px}
.cat .rate{margin:8px 0 0 20px;font-size:9px;color:var(--muted)}
.cat .rate span{color:var(--orange);letter-spacing:1px}
.cat .foot{position:absolute;left:20px;right:20px;bottom:20px;display:flex;justify-content:space-between;align-items:center;font-size:10px;color:var(--ink)}
.cat .book{border:1px solid var(--line);padding:7px 14px;font-size:9px;font-weight:500}
.tile{position:absolute;overflow:hidden}
.tile .ov{position:absolute;color:var(--white);line-height:1}
.gal-big{font-size:31px;left:18px;bottom:20px;line-height:33px}
.gal-tall{font-size:24px;left:16px;top:18px;line-height:25px;color:rgba(255,255,255,.85)}

/* testimonials */
.testi{height:517px;background:linear-gradient(180deg,#17244d 0%,#1a2b57 50%,#141f44 100%)}
.testi .sec-head{padding-top:68px}
.testi .script{color:var(--white)}
.testi h2{color:var(--white)}
.quote{left:183px;top:178px;width:834px;height:219px;background:var(--white)}
.quote .avatar{left:24px;top:36px;width:63px;height:63px;border-radius:50%;background:linear-gradient(135deg,#d9dde6,#b8bfcc)}
.quote p{position:absolute;left:111px;top:40px;width:680px;font-size:9.4px;line-height:18px;color:var(--text)}
.dots{left:586px;top:434px;display:flex;gap:6px}
.dots i{width:9px;height:9px;border-radius:50%;background:var(--blue);display:block}
.dots i+i{background:var(--white)}

/* blog */
.blog{height:652px}
.blog .sec-head{padding-top:68px}
.post{top:167px;width:265px}
.post .pic{position:relative;height:227px}
.post .date{position:absolute;left:0;top:0;width:62px;height:55px;background:var(--white);text-align:center;font-size:8px;line-height:10px;padding-top:5px;color:var(--muted)}
.post .date b{display:block;font-size:20px;line-height:22px;color:var(--brand-blue)}
.post .meta{font-size:8.5px;margin-top:26px;color:var(--muted)}
.post .meta em{font-style:normal;color:var(--orange)}
.post h3{font-size:16px;line-height:19px;margin-top:6px}
.post p{font-size:8.6px;line-height:16px;margin-top:10px}
.post .more{display:inline-flex;gap:6px;border:1px solid var(--line);padding:8px 16px;font-size:9px;font-weight:600;color:var(--ink);margin-top:18px}

/* footer */
.footer{height:350px;background:var(--navy);color:#c3c8d8}
.footer .brand{left:185px;top:42px;font-size:19px;font-weight:600;color:var(--white)}
.stat{top:36px;display:flex;gap:12px;align-items:flex-start}
.stat .ico{width:32px;height:32px;border:1.5px solid #8f97b3;border-radius:6px}
.stat b{display:block;color:var(--white);font-size:17px;font-weight:600;line-height:20px}
.stat span{font-size:9.5px}
.col{top:128px;font-size:9.5px;line-height:26px}
.col h4{font-family:"DM Serif Text",serif;color:var(--white);font-size:12px;font-weight:400;line-height:14px;margin-bottom:8px}
.col.touch{line-height:12px;width:270px}
.col.touch p{font-size:8.6px;line-height:11px}
.col.touch .row{display:flex;gap:10px;align-items:center;margin-top:10px;font-size:9.5px}
.col.news p{font-size:9px;line-height:16px;width:230px}
.subscribe{display:flex;margin-top:12px;width:224px;height:30px}
.subscribe .in{flex:1;background:var(--white);font-size:9px;color:var(--muted);display:flex;align-items:center;padding-left:30px}
.subscribe .sb{width:43px;background:var(--blue);display:flex;align-items:center;justify-content:center}
.copy{left:188px;top:312px;font-size:9.5px}
.fsocial{right:190px;top:312px;display:flex;gap:14px}
.fsocial i{width:10px;height:10px;border-radius:50%;background:#c3c8d8;display:block}
</style>
</head>
<body>

<header class="topbar">
  <div class="abs ask">Have Any Questions?: <b>+57 300 555 0142</b></div>
  <div class="abs tag">Trusted Panama Charter Specialists with a Passion for San Blas</div>
  <div class="abs social"><i></i><i></i><i></i><i></i></div>
  <div class="abs lang">EN / Fr</div>
</header>

<nav class="nav">
  <div class="abs logo"><span class="mark"></span><span class="name">Coral Hop Voyages</span></div>
  <div class="abs menu"><span>Home</span><span>Sailboat Trips</span><span>Boats</span><span>How It Works</span><span>Blog</span><span>Contact Us</span></div>
  <div class="abs cta-nav">CHARTER INQUIRY FORM</div>
</nav>

<section class="hero">
  <div class="abs bg" role="img" aria-label="Aerial view of a motor yacht carving a wake across dark blue sea"></div>
  <div class="abs script">Let's Feel a Yacht Trip</div>
  <h1 class="serif">Find a Yacht today</h1>
  <div class="abs search">
    <div class="field"><span class="ic"></span><div><div class="lbl">Check in</div><div class="val">dd-mm-yyyy</div></div></div>
    <div class="field"><span class="ic"></span><div><div class="lbl">Check out</div><div class="val">dd-mm-yyyy</div></div></div>
    <div class="field"><span class="ic" style="border-radius:50%"></span><div><div class="lbl">Guests</div><div class="val">3 Persons</div></div></div>
    <div class="go"><svg width="11" height="11" viewBox="0 0 12 12"><circle cx="5" cy="5" r="3.8" fill="none" stroke="#fff" stroke-width="1.4"/><path d="M8 8l3 3" stroke="#fff" stroke-width="1.4"/></svg>Search</div>
  </div>
</section>

<section class="about">
  <div class="photo" style="left:183px;top:143px;width:116px;height:116px;background:linear-gradient(160deg,#2fb3b8,#137f8f)" role="img" aria-label="Speedboat on turquoise water seen from above"></div>
  <div class="photo" style="left:325px;top:41px;width:302px;height:271px;background:linear-gradient(180deg,#2c2f48 0%,#a8532b 45%,#e98a2c 55%,#3a3046 100%)" role="img" aria-label="Sunset over a palm island"></div>
  <div class="photo" style="left:220px;top:336px;width:339px;height:222px;background:linear-gradient(180deg,#6fb6e0 0%,#2f7a3f 40%,#3fc2c0 62%,#1d9fb0 100%)" role="img" aria-label="Tropical island beach with palm trees and clear water"></div>
  <div class="abs txt">
    <div class="script">About Us</div>
    <h2 class="serif">Providing Large<br>Yachts For A Perfect</h2>
    <p>We're sailors and travelers with a love for exploration. When we first arrived in San Blas, its unique beauty and culture left a lasting impression. What began as a stop along our journey soon became something more—we felt a strong connection to this place and a sincere respect for its people, traditions, and way of life. Rather than simply making it our home, we've done our best to live in harmony with the environment and the values of the local community.</p>
    <p>Today, our mission is to share the experience of San Blas with others through safe, sustainable, and memorable sailing adventures.</p>
    <p>We do this by building trusted partnerships, ensuring the visitors we bring maintain a respectful presence, and guiding every trip with care, cultural sensitivity, and a commitment to quality.</p>
    <a class="btn-blue">Get Started</a>
  </div>
</section>

<section class="services-head sec-head">
  <span class="script">Our Services</span>
  <h2 class="serif">Discover Ultimate Panama Sailing Tours</h2>
</section>

<section class="services">
  <article class="abs svc" style="left:202px">
    <div class="pic" style="background:linear-gradient(180deg,#6aa7dc 0%,#dfe8ef 55%,#2d6c8a 100%)" role="img" aria-label="White sailing yacht moored at a dock"></div>
    <h3 class="serif">Private Charters</h3>
    <p>Sail the beautiful islands and beaches of San Blas on a private all-inclusive catamaran. Enjoy a custom itinerary, friendly crew, and flexible options to fit any budget—perfect for a relaxing escape.</p>
  </article>
  <article class="abs svc" style="left:480px">
    <div class="pic" style="background:linear-gradient(180deg,#b9d6ef 0%,#e9eef2 50%,#6d7f8c 100%)" role="img" aria-label="Guests relaxing on the deck of a sailboat"></div>
    <h3 class="serif">Shared Charters</h3>
    <p>Share the experience with others for a more affordable alternative to a private charter. Perfect for couples, solo travelers, and small groups—enjoy San Blas beaches, clear waters, great meals, and a relaxed atmosphere with a welcoming crew.</p>
  </article>
  <article class="abs svc" style="left:759px">
    <div class="pic" style="background:linear-gradient(180deg,#7bb9e6 0%,#1a88b8 45%,#0f6f9e 100%)" role="img" aria-label="Catamaran with red deck on blue water"></div>
    <h3 class="serif">Family Friendly<br>Boat Trips</h3>
    <p>San Blas is perfect for kids, with calm waters, safe snorkeling, and fun island-hopping. Families love the mix of adventure and culture—an ideal way to explore Panama together.</p>
  </article>
</section>

<section class="fleet">
  <div class="sec-head">
    <span class="script">Our Exclusives</span>
    <h2 class="serif">Featured Catamarans</h2>
  </div>

  <article class="abs cat" style="left:190px">
    <div class="pic" style="background:linear-gradient(180deg,#5f9ed6 0%,#8fbbe0 45%,#2a5f8a 100%)" role="img" aria-label="Large white motor yacht near a green coastline">
      <span class="badge">Featured</span>
      <svg class="heart" viewBox="0 0 14 14"><path d="M7 12S1.5 8.5 1.5 4.8A2.8 2.8 0 0 1 7 3.6a2.8 2.8 0 0 1 5.5 1.2C12.5 8.5 7 12 7 12z" fill="none" stroke="#fff" stroke-width="1.1"/></svg>
      <div class="stats"><span>5 Star</span><span>13 People</span><span>2022</span><span>30″ft</span></div>
    </div>
    <h3>Corsica 42</h3>
    <div class="rate"><span>★★★★★</span> (4.50 rating)</div>
    <div class="foot"><span>Info &amp; Price</span><span class="book">Book Now →</span></div>
  </article>

  <article class="abs cat" style="left:475px">
    <div class="pic" style="background:linear-gradient(180deg,#8db8dc 0%,#c9dbe8 45%,#2e6d94 100%)" role="img" aria-label="White flybridge yacht cruising at sea">
      <span class="badge">Featured</span>
      <svg class="heart" viewBox="0 0 14 14"><path d="M7 12S1.5 8.5 1.5 4.8A2.8 2.8 0 0 1 7 3.6a2.8 2.8 0 0 1 5.5 1.2C12.5 8.5 7 12 7 12z" fill="none" stroke="#fff" stroke-width="1.1"/></svg>
      <div class="stats"><span>4 Star</span><span>19 People</span><span>2022</span><span>50″ft</span></div>
    </div>
    <h3>Marlin 55F</h3>
    <div class="rate"><span>★★★★★</span> (5.00 rating)</div>
    <div class="foot"><span>Info &amp; Price</span><span class="book">Book Now →</span></div>
  </article>

  <article class="abs cat" style="left:759px">
    <div class="pic" style="background:linear-gradient(180deg,#9fb6c9 0%,#c7d3dc 45%,#3c5b76 100%)" role="img" aria-label="Sailboat under full sail on open water">
      <div class="added">♥ Product added!<br>View wishlist</div>
      <div class="stats"><span>4 Star</span><span>19 People</span><span>2014</span><span>30″ft</span></div>
    </div>
    <h3>Marlin 55S</h3>
    <div class="rate"><span>★★★★★</span> (5.00 rating)</div>
    <div class="foot"><span>Info &amp; Price</span><span class="book">Book Now →</span></div>
  </article>

  <div class="tile" style="left:198px;top:564px;width:399px;height:236px;background:linear-gradient(160deg,#1f5d84 0%,#3aa5b5 45%,#1b6e8e 100%)" role="img" aria-label="Aerial view of a small island ringed by reef">
    <div class="ov gal-big">Special<br>Offers</div>
  </div>
  <div class="tile" style="left:617px;top:564px;width:190px;height:108px;background:linear-gradient(180deg,#5fa6dc,#2ab3c3)" role="img" aria-label="Catamaran anchored off a beach"></div>
  <div class="tile" style="left:617px;top:692px;width:190px;height:108px;background:linear-gradient(180deg,#4f98d0,#1aa6b8)" role="img" aria-label="Catamaran in turquoise shallows"></div>
  <div class="tile" style="left:826px;top:564px;width:189px;height:236px;background:linear-gradient(180deg,#5aa0d6 0%,#3b8c4a 30%,#1f9fb8 60%,#1a7fa8 100%)" role="img" aria-label="Sailboat near a palm-lined shore">
    <div class="ov gal-tall">Special<br>Offers</div>
  </div>
  <div class="tile" style="left:198px;top:821px;width:190px;height:106px;background:linear-gradient(180deg,#2b7c9c,#1a5a74)" role="img" aria-label="Friends swimming in the sea"></div>
  <div class="tile" style="left:198px;top:949px;width:190px;height:108px;background:linear-gradient(180deg,#8fb5d6,#4a93b0)" role="img" aria-label="Catamaran with dinghy on calm water"></div>
  <div class="tile" style="left:407px;top:821px;width:190px;height:236px;background:linear-gradient(180deg,#4a90d0 0%,#2b7cb0 55%,#0f5c86 100%)" role="img" aria-label="Sailing catamaran on deep blue sea"></div>
  <div class="tile" style="left:617px;top:821px;width:398px;height:236px;background:linear-gradient(160deg,#1c9fc0 0%,#45b7cf 45%,#1d6d96 100%)" role="img" aria-label="Snorkeler swimming among tropical fish">
    <div class="ov" style="left:22px;bottom:42px;font-size:30px">Weekly Flash Deals</div>
    <div class="ov" style="left:26px;bottom:18px;font-size:17px">Up to 30% off</div>
  </div>
</section>

<section class="testi">
  <div class="sec-head">
    <span class="script">Testimonials</span>
    <h2 class="serif">What Customer Say</h2>
  </div>
  <div class="abs quote">
    <div class="abs avatar" role="img" aria-label="Customer portrait"></div>
    <p>Absolutely phenomenal experience. We have traveled all around the world and this was one of the best experiences we have ever had. From the beginning of the booking process with Teodora and being matched with a boat and captain, all my questions were readily answered. They made sure everything was taken care of and all handoffs to all logistics partners were seamless. Our captain Oriel and cook Valeska and first mate Maren went over and beyond to make sure our young kids were looked after, well fed, entertained, and even helped to bathe them. They cared about our overall experience and cooked some amazing, fresh food. This is truly a once in a lifetime experience and the islands are truly breathtaking. I highly recommend this trip, and through this company and truly appreciate everything they did to make a lifetime of memories for my family.</p>
  </div>
  <div class="abs dots"><i></i><i></i></div>
</section>

<section class="blog">
  <div class="sec-head">
    <span class="script">Our Blog</span>
    <h2 class="serif">Blog &amp; Articles</h2>
  </div>
  <article class="abs post" style="left:183px">
    <div class="pic" style="background:linear-gradient(180deg,#9cb4c9 0%,#d8dde2 50%,#3c6e88 100%)" role="img" aria-label="Yacht moored beside a luxury poolside terrace">
      <div class="date">2022<b>6</b>April</div>
    </div>
    <div class="meta"><em>Boat, Marine</em>No Comments</div>
    <h3 class="serif">5 Tips to Increase Your Online Sales</h3>
    <p>Lorem ipsum dolor sit amet, consectetur adipiscing elit, sed do eiusmod tempor incididunt ut labore et dolore magna aliqua. Ut enim ad minim</p>
    <a class="more">Read more →</a>
  </article>
  <article class="abs post" style="left:467px">
    <div class="pic" style="background:linear-gradient(180deg,#b9d3ea 0%,#a9c6dc 55%,#5a8a9e 100%)" role="img" aria-label="Sailboat at anchor in a calm bay">
      <div class="date">2022<b>19</b>February</div>
    </div>
    <div class="meta"><em>Boat, Marine</em>No Comments</div>
    <h3 class="serif">The Harbourview Collection by Nora Lindqvist</h3>
    <p>Lorem ipsum dolor sit amet, consectetur adipiscing elit, sed do eiusmod tempor incididunt ut labore et dolore magna aliqua. Ut enim ad minim</p>
    <a class="more">Read more →</a>
  </article>
  <article class="abs post" style="left:752px">
    <div class="pic" style="background:linear-gradient(180deg,#8fb8d8 0%,#d9e3ea 45%,#35698c 100%)" role="img" aria-label="Sailor at the helm of a yacht">
      <div class="date">2022<b>19</b>March</div>
    </div>
    <div class="meta"><em>Marine</em>No Comments</div>
    <h3 class="serif">Given Set was without from god divide rule Hath</h3>
    <p>Lorem ipsum dolor sit amet, consectetur adipiscing elit, sed do eiusmod tempor incididunt ut labore et dolore magna aliqua. Ut enim ad minim</p>
    <a class="more">Read more →</a>
  </article>
</section>

<footer class="footer">
  <div class="abs brand">Coral Hop Voyages</div>
  <div class="abs stat" style="left:352px"><span class="ico"></span><div><b>657</b><span>Satisfied Clients</span></div></div>
  <div class="abs stat" style="left:518px"><span class="ico"></span><div><b>342</b><span>Luxurious Boats</span></div></div>
  <div class="abs stat" style="left:684px"><span class="ico"></span><div><b>120</b><span>Experienced Crew</span></div></div>
  <div class="abs stat" style="left:848px"><span class="ico"></span><div><b>231</b><span>Premium Facilities</span></div></div>

  <div class="abs col touch" style="left:188px">
    <h4>Get in touch</h4>
    <p>Discover unforgettable catamaran and sailboat adventures in Guna Yala (San Blas), Panama. Coral Hop Voyages LLC offers all-inclusive island-hopping, snorkeling, and immersive cultural experiences—trusted by travelers worldwide.</p>
    <div class="row"><svg width="12" height="10" viewBox="0 0 12 10"><rect x=".6" y=".6" width="10.8" height="8.8" fill="none" stroke="#c3c8d8"/><path d="M.6.8 6 5.5 11.4.8" fill="none" stroke="#c3c8d8"/></svg>hello@coralhopvoyages.net</div>
    <div class="row"><svg width="12" height="12" viewBox="0 0 12 12"><path d="M2 1h2.5l1 3-1.5 1a7 7 0 0 0 3 3l1-1.5 3 1V10a1 1 0 0 1-1 1A10 10 0 0 1 1 2a1 1 0 0 1 1-1z" fill="none" stroke="#c3c8d8"/></svg>+57 300 555 0187</div>
  </div>
  <div class="abs col" style="left:499px">
    <h4>Company</h4>
    <div>Yacht Rent</div><div>About Us</div><div>Services</div><div>Blog</div>
  </div>
  <div class="abs col" style="left:610px">
    <h4>Discover</h4>
    <div>FAQ's</div><div>Contact Us</div><div>Privacy Policy</div><div>Refund and Returns Policy</div>
  </div>
  <div class="abs col news" style="left:788px">
    <h4>Newsletter</h4>
    <p>Sign up to receive weekly deals, valuable information and more.</p>
    <div class="subscribe"><div class="in">Enter your email...</div><div class="sb"><svg width="10" height="10" viewBox="0 0 10 10"><path d="M1 5h8M6 2l3 3-3 3" fill="none" stroke="#fff" stroke-width="1.3"/></svg></div></div>
  </div>

  <div class="abs copy">Copyright 2022 © Coral Hop Voyages</div>
  <div class="abs fsocial"><i></i><i></i><i></i><i></i></div>
</footer>

</body>
</html>
```